Poster for an advertising campaign

Hi, we are an agency, our business is to orienteates student to study abroad in Germany. For that, we enroll them in language schools in Germany and help them to find an accomodation.
We are going to launch an advertising campaign through Rural advertising signs.
- Need to have our Morvalin Center logo
- Need to have these 2 mentions :
1/ Etudes en Allemagne et accompagnement durant toute la procédure.
2/ Cours de langue allemande
- If possible put as a signature ; in small characters our brand essence ( Excellence Through Education ) Maybe at the bottom right of the logo
For the format it will be 3.5m*2.5m , more format adaptations will be shared as soon as we finalize the crea
- We would like to have the logo in 2D ,like for the attached simulation
- Need to have interesting backgrounds and designs in line with our identity & service ( studying in Germany , learn the German language , the support &the accompaniment during all the procedure …) ,knowing as well that our target is bachelors , bac students …
Thx

```html
<!DOCTYPE html>
<html lang="fr">
<head>
<meta charset="utf-8">
<title>Morvalin Center — Etudes en Allemagne</title>
<link rel="stylesheet" href="https://fonts.googleapis.com/css2?family=Roboto+Condensed:wght@700&display=swap">
<style>
  :root {
    --wood: #a39886;
    --wood-dark: #7d7262;
    --flag-black: #1a1410;
    --flag-red: #d9141c;
    --flag-gold: #e0a21a;
    --logo-yellow: #d8d62a;
    --text-white: #ffffff;
    --photo-light: #c9b8a4;
    --photo-shirt: #8fa9c8;
  }
  html, body {
    margin: 0;
    padding: 0;
    width: 1200px;
    height: 858px;
    overflow: hidden;
    background: var(--wood);
  }
  .poster {
    position: relative;
    width: 1200px;
    height: 858px;
    overflow: hidden;
    background: linear-gradient(180deg, var(--wood) 0%, var(--wood-dark) 100%);
    font-family: "Roboto Condensed", "Arial Narrow", sans-serif;
    font-weight: 700;
    color: var(--text-white);
  }
  .flag-band { position: absolute; left: 0; width: 1200px; }
  .flag-band--black { top: 40px; height: 240px; background: var(--flag-black); }
  .flag-band--red { top: 275px; height: 305px; background: var(--flag-red); }
  .flag-band--gold {
    top: 578px; height: 200px;
    background: linear-gradient(180deg, var(--flag-gold) 0%, #c98d14 100%);
  }
  .student-photo {
    position: absolute;
    left: 220px;
    top: 96px;
    width: 440px;
    height: 762px;
    border-radius: 180px 180px 0 0;
    background: linear-gradient(180deg, var(--photo-light) 0%, var(--photo-shirt) 45%, #a7b9cf 100%);
  }
  .brand {
    position: absolute;
    left: 38px;
    top: 172px;
    display: flex;
    align-items: center;
    gap: 18px;
  }
  .brand__dot {
    width: 56px;
    height: 56px;
    border-radius: 50%;
    background: var(--logo-yellow);
  }
  .brand__name {
    font-size: 54px;
    line-height: 1;
    color: var(--text-white);
    letter-spacing: 0.5px;
  }
  .message {
    position: absolute;
    left: 678px;
    margin: 0;
    font-size: 36px;
    line-height: 48px;
    letter-spacing: 0.2px;
  }
  .message--studies { top: 298px; }
  .message--courses { top: 500px; }
  .signature {
    position: absolute;
    left: 678px;
    top: 782px;
    margin: 0;
    font-size: 32px;
    line-height: 40px;
  }
</style>
</head>
<body>
  <main class="poster">
    <div class="flag-band flag-band--black"></div>
    <div class="flag-band flag-band--red"></div>
    <div class="flag-band flag-band--gold"></div>

    <div class="student-photo" role="img" aria-label="Photo d'un étudiant souriant en chemise à carreaux tenant un cahier jaune"></div>

    <div class="brand">
      <span class="brand__dot"></span>
      <span class="brand__name">Morvalin Center</span>
    </div>

    <p class="message message--studies">Etudes en Allemagne et<br>accompagnement<br>durant toute la procédure.</p>
    <p class="message message--courses">Cours de langue allemande</p>

    <p class="signature">Excellence Through Education</p>
  </main>
</body>
</html>
```